Business card for Full Stable Care Vandorpe

I would like to have me designed an professional business card with my existing logo for my company called : full stable care vandorpe gcv.
I prefer a two sided business card with on the back side only the horses head and the website : fscvandorpe-example.eu
Only one colour shouldbe all right.
The logo must appear in a nic professional way on the business card.

Other suggestion are welcome.

All copy wrights must be released by the designer after we have selected a final design.

Target Market(s)

Equestrian businesses

Industry/Entity Type

Business

Contact Information for Business Card

Laurent Vandorpe
Title: zaakvoerder
Full Stable Care Vandorpe GCV
Molkenweg 47
B - 2870 Lindenvelde
België
Phone: + 32 491 68 27 04
Mail: laurent@fscvandorpe-example.eu

Font styles to use
Serif

Requirements
Must have
• My own logo
• See attached files
• Website: fscvandorpe-example.eu

```html
<!DOCTYPE html>
<html lang="nl">
<head>
<meta charset="utf-8">
<title>Full Stable Care Vandorpe – Visitekaartje</title>
<link href="https://fonts.googleapis.com/css2?family=Noto+Serif:wght@400;700&display=swap" rel="stylesheet">
<style>
  :root {
    --stage: #2e2e2e;
    --card-dark: #4a4a4a;
    --card-light: #ffffff;
    --ink: #1a1a1a;
    --ink-soft: #333333;
    --on-dark: #f2f2f2;
    --rule: #3a3a3a;
  }
  * { margin: 0; padding: 0; box-sizing: border-box; }
  html, body {
    width: 1200px; height: 900px; overflow: hidden;
    background: var(--stage);
    font-family: "Noto Serif", Georgia, serif;
  }
  .stage { position: relative; width: 1200px; height: 900px; }
  .card {
    position: absolute; top: 285px;
    width: 540px; height: 330px;
    border-radius: 18px; overflow: hidden;
    box-shadow: 0 10px 30px rgba(0,0,0,.35);
  }

  /* Back side */
  .card-back { left: 40px; background: var(--card-dark); }
  .back-mark {
    position: absolute; left: 0; right: 0; top: 110px;
    display: flex; flex-direction: column; align-items: center; gap: 14px;
  }
  .back-mark .dot {
    width: 54px; height: 54px; border-radius: 50%;
    background: #8c8c8c;
  }
  .back-mark .brand-name {
    font-size: 22px; font-weight: 700; color: #bdbdbd; letter-spacing: .5px;
  }
  .back-site {
    position: absolute; left: 0; right: 0; bottom: 28px;
    text-align: center; font-size: 13px; color: var(--on-dark);
  }

  /* Front side */
  .card-front { left: 620px; background: var(--card-light); }
  .card-front svg.band { position: absolute; inset: 0; }
  .front-brand {
    position: absolute; right: 34px; top: 38px;
    font-size: 18px; font-weight: 700; color: var(--ink);
  }
  .brand-rule {
    position: absolute; left: 190px; right: 34px; top: 72px;
    height: 1px; background: var(--rule);
  }
  .corner-mark {
    position: absolute; right: 40px; top: 132px;
    width: 78px; height: 78px; border-radius: 50%;
    background: var(--card-light);
  }
  .person { position: absolute; left: 30px; top: 118px; width: 330px; }
  .person .name { font-size: 22px; color: var(--ink); line-height: 1.2; }
  .person .name-rule { height: 1px; background: var(--rule); margin: 4px 0 6px; }
  .person .role { font-size: 13px; color: var(--ink-soft); }
  .person .address { font-size: 13px; color: var(--ink-soft); line-height: 1.4; margin-top: 2px; }
  .contact {
    position: absolute; left: 30px; top: 262px;
    list-style: none; font-size: 12.5px; color: var(--on-dark);
  }
  .contact li { display: flex; align-items: center; gap: 10px; line-height: 20px; }
  .contact svg { width: 12px; height: 12px; fill: none; stroke: var(--on-dark); stroke-width: 1.6; }
</style>
</head>
<body>
<main class="stage">

  <section class="card card-back" aria-label="Achterkant visitekaartje">
    <div class="back-mark">
      <span class="dot"></span>
      <span class="brand-name">Full Stable Care Vandorpe</span>
    </div>
    <p class="back-site">www.fscvandorpe-example.eu</p>
  </section>

  <section class="card card-front" aria-label="Voorkant visitekaartje">
    <svg class="band" width="540" height="330" viewBox="0 0 540 330" aria-hidden="true">
      <path d="M0 248 H370 Q388 248 390 230 V132 Q392 112 412 112 H540 V330 H0 Z" fill="var(--card-dark)"/>
    </svg>

    <div class="front-brand">Full Stable Care Vandorpe</div>
    <div class="brand-rule"></div>
    <span class="corner-mark"></span>

    <div class="person">
      <p class="name">Laurent Vandorpe</p>
      <div class="name-rule"></div>
      <p class="role">Zaakvoerder</p>
      <p class="address">Molkenweg 47<br>B - 2870 Lindenvelde<br>België</p>
    </div>

    <ul class="contact">
      <li>
        <svg viewBox="0 0 12 12"><path d="M2 1.5 L4 1.5 L5 4 L3.8 5 Q5 7.5 7 8.2 L8 7 L10.5 8 L10.5 10 Q6 11 2.5 7 Q1 4.5 2 1.5 Z"/></svg>
        + 32 491 68 27 04
      </li>
      <li>
        <svg viewBox="0 0 12 12"><rect x="1" y="2.5" width="10" height="7"/><path d="M1 2.5 L6 6.5 L11 2.5"/></svg>
        laurent@fscvandorpe-example.eu
      </li>
      <li>
        <svg viewBox="0 0 12 12"><circle cx="6" cy="6" r="4.8"/><path d="M1.2 6 H10.8 M6 1.2 Q3.5 6 6 10.8 M6 1.2 Q8.5 6 6 10.8"/></svg>
        www.fscvandorpe-example.eu
      </li>
    </ul>
  </section>

</main>
</body>
</html>
```